accomplished personal trainer, former elite gymnast from Russia, highly professional and experienced

Established Fitness trainer in California requires a new web site to attract personal clients and build her group exercise classes.

Here is an example of another fitness trainer's site that I really liked the technology:
http://www.tedvolmar.com

Below I have inserted my current web site: www.qorelafitnessvale.com
You can use this web site for the principal content, such as my background and qualifications.

Target Market(s)

Anyone who wants to improve their fitness levels and wellness in general. Anyone who needs directions and instruction on how to exercise. I can train anyone from elite athlete to a disabled person.

Industry/Entity Type

Fitness

Coding

Coded - Design and coding required

Number of Pages Required

5+ page

Font styles to use
Sans Serif

Requirements
Must have
• Easy to navigate main info about me, location, services, contact, benefits of using my services.
• Would be great to create unique representation of me as a trainer and a person, using new technologies and new ideas. Make it different from the other websites. Having its own character. Not too complicated and heavy with information, but an eye catching, useful and fun to navigate.
Nice to have
• new technology, easy access to information, the idea of enjoyment of life, lightness about achieving any goal, spiritual wisdom, unique design. I am planning to insert educational videos, advise, maybe jokes. Sign in, shopping cart, logo, should be easy for me to make changes in content.
Should not have
• cliché, outdated technology, too complicated,

```html
<!DOCTYPE html>
<html lang="en">
<head>
<meta charset="utf-8">
<title>Qorela Fitness Vale</title>
<link href="https://fonts.googleapis.com/css2?family=Nunito+Sans:wght@300;400;600;700;800&family=Open+Sans:wght@400;600&display=swap" rel="stylesheet">
<style>
:root{
  --orange:#f07c00;
  --orange-dark:#e06f00;
  --teal:#2bbdb0;
  --teal-deep:#1fa79b;
  --ink:#222;
  --text:#555;
  --muted:#888;
  --light:#ececec;
  --footer:#2a2a2a;
  --white:#fff;
}
*{box-sizing:border-box;margin:0;padding:0}
html,body{width:1200px;height:3838px;overflow:hidden}
body{font-family:"Open Sans",Arial,sans-serif;color:var(--text);background:var(--white)}
h1,h2,h3,h4,.brand,.nav a,.btn{font-family:"Nunito Sans",Arial,sans-serif}
.wrap{width:980px;margin:0 auto;position:relative}

.topbar{height:102px}
.topbar .wrap{display:flex;justify-content:space-between;align-items:center;height:102px}
.brand{font-size:25px;font-weight:800;letter-spacing:2px;color:var(--ink)}
.contact-mini{text-align:right;padding-right:8px}
.contact-mini span{display:block;color:var(--orange);font-size:15px;letter-spacing:1px}
.contact-mini strong{display:block;font-weight:400;font-size:23px;color:var(--ink);letter-spacing:1px}

.nav{height:59px;background:linear-gradient(var(--orange),var(--orange-dark))}
.nav .wrap{display:flex;align-items:center;height:59px;gap:0}
.nav a{color:var(--white);text-decoration:none;font-size:15px;font-weight:600;padding:10px 18px;letter-spacing:.5px}
.nav a.active{border:1px solid rgba(255,255,255,.85)}

.hero{position:relative;height:484px;background:linear-gradient(180deg,#5c7a3a 0%,#7fa24a 45%,#5f8a2e 100%)}
.hero-copy{position:absolute;top:120px;left:0;right:0;text-align:center;color:var(--white)}
.hero-copy .welcome{font-family:"Nunito Sans",sans-serif;font-weight:300;font-size:72px;letter-spacing:4px;color:transparent;-webkit-text-stroke:2px var(--white);line-height:1}
.hero-copy .title{font-family:"Nunito Sans",sans-serif;font-weight:700;font-size:64px;letter-spacing:2px;line-height:1.1}
.btn-outline-light{display:inline-block;margin-top:26px;border:2px solid var(--white);color:var(--white);padding:12px 28px;font-size:15px;letter-spacing:1px}
.dots{position:absolute;bottom:22px;left:0;right:0;text-align:center}
.dots i{display:inline-block;width:14px;height:14px;border-radius:50%;background:rgba(255,255,255,.9);margin:0 3px}
.dots i:first-child{background:none;border:2px solid var(--white)}

.quote{position:relative;height:232px;background:var(--orange);color:var(--white);text-align:center}
.quote p{width:1000px;margin:0 auto;padding-top:50px;font-size:21px;line-height:32px}
.quote::after{content:"";position:absolute;bottom:-22px;left:580px;border:22px solid transparent;border-top-color:var(--orange);border-bottom:0}

.photo{display:block}
.photo-group{height:343px;background:linear-gradient(90deg,#6c7d52,#8aa660 50%,#5d7644)}

.about{height:425px}
.about .wrap{display:flex;gap:42px;padding-top:45px;padding-left:22px}
.about-photo{flex:0 0 315px;height:327px;border-radius:14px;background:linear-gradient(160deg,#8ab35a,#5e8b3c)}
.about h2{font-size:38px;font-weight:600;color:var(--ink);margin:2px 0 18px}
.about p{font-size:14.5px;line-height:26px;margin-bottom:18px;width:560px}
.btn-dark{display:inline-block;margin-top:10px;background:#3b3b3b;color:var(--white);border:3px solid #aaa;outline:2px solid #3b3b3b;padding:12px 30px;font-size:14px;font-weight:700}

.photo-stretch{height:383px;background:linear-gradient(90deg,#4c5a3c,#6c7b63 40%,#3e4b47)}

.services{height:432px;background:var(--light)}
.services .wrap{display:flex;gap:80px;padding-top:35px;padding-left:38px}
.service{width:400px;position:relative}
.service svg.hex{position:absolute;top:0;left:-36px}
.service .icon{position:absolute;top:70px;left:32px}
.service h3{position:relative;margin-top:140px;font-size:27px;font-weight:700;color:var(--ink)}
.service p{font-size:14.5px;line-height:25px;margin:14px 0 24px;width:390px}
.btn-outline{display:inline-block;border:1px solid #888;background:var(--white);padding:10px 32px;font-size:14px;font-weight:700;color:var(--ink)}

.videos{height:392px;background:linear-gradient(90deg,var(--teal-deep),var(--teal) 50%,var(--teal-deep));text-align:center}
.videos h2{color:var(--white);font-size:31px;font-weight:700;padding-top:36px}
.video-row{display:flex;justify-content:space-between;width:1000px;margin:26px auto 0}
.video{width:312px;height:210px;border:5px solid var(--white);position:relative}
.video svg{position:absolute;top:50%;left:50%;transform:translate(-50%,-50%)}
.v1{background:linear-gradient(135deg,#7c9a4a,#c9a9b8)}
.v2{background:linear-gradient(135deg,#7a5a3c,#a47b55)}
.v3{background:linear-gradient(135deg,#6e5b4b,#b49676)}

.news{height:363px}
.news h2{color:var(--orange);font-size:33px;font-weight:700;padding-top:62px}
.news-row{display:flex;gap:44px;margin-top:38px}
.news-item{width:300px}
.news-item h4{font-size:19px;font-weight:600;color:var(--ink);line-height:25px;margin-bottom:8px}
.news-item p{font-size:13.5px;line-height:23px;color:var(--muted)}
.news-item a{display:block;margin-top:4px;font-size:13px;font-weight:700;color:var(--orange);text-decoration:none}

.photo-team{height:328px;background:linear-gradient(90deg,#4a6a35,#7b9b52 50%,#3e5a2c)}

.newsletter{height:148px;background:#e6e6e6}
.newsletter .wrap{display:flex;align-items:center;height:148px;gap:18px}
.newsletter h3{font-size:29px;font-weight:700;color:#444;width:325px}
.newsletter h3 span{color:var(--muted);font-weight:400}
.newsletter input{width:237px;height:50px;border:none;background:var(--white);padding:0 16px;font-size:14px;font-family:inherit}
.btn-teal{background:var(--teal);color:var(--white);height:50px;padding:0 28px;border:2px solid #9fe0d9;font-weight:700;font-size:15px;display:flex;align-items:center}

.footer{height:147px;background:var(--footer);color:#ddd}
.footer .wrap{padding-top:46px}
.footer-nav{display:flex;gap:36px}
.footer-nav a{color:var(--white);text-decoration:none;font-size:15px;font-family:"Nunito Sans",sans-serif}
.footer small{display:block;margin-top:14px;font-size:12px;color:#aaa}
.social{position:absolute;right:0;top:40px;display:flex;gap:8px}
.social i{width:32px;height:32px;border:2px solid #ddd;border-radius:50%}
</style>
</head>
<body>

<header class="topbar">
  <div class="wrap">
    <div class="brand">QORELA FITNESS VALE</div>
    <div class="contact-mini"><span>CONTACT US</span><strong>(555) 214 7730</strong></div>
  </div>
</header>

<nav class="nav">
  <div class="wrap">
    <a class="active" href="#">HOME</a>
    <a href="#">GROUP CLASSES</a>
    <a href="#">PERSONAL TRAINING</a>
    <a href="#">ABOUT QORELA</a>
    <a href="#">BLOG</a>
    <a href="#">CONTACT</a>
  </div>
</nav>

<section class="hero" role="img" aria-label="Trainer stretching in a split on a sunny lawn">
  <div class="hero-copy">
    <div class="welcome">WELCOME</div>
    <div class="title">FITNESS OUTDOORS</div>
    <span class="btn-outline-light">CONTACT US</span>
  </div>
  <div class="dots"><i></i><i></i><i></i><i></i></div>
</section>

<section class="quote">
  <p>I have known Mira for many years as a fitness trainer and workout class instructor. She is truly one of the very best in the business. Mira is extremely knowledgeable about human physiology and teaching. Her personality is professional, informative, and caring. She would always put "her all" into each of her classes.</p>
</section>

<div class="photo photo-group" role="img" aria-label="Group class doing squats together in a park"></div>

<section class="about">
  <div class="wrap">
    <div class="about-photo" role="img" aria-label="Portrait of the trainer standing on grass"></div>
    <div>
      <h2>About Qorela Fitness</h2>
      <p>Mira Solvane is the owner of Qorela Fitness. She was born and raised in Vologda, Russia where she was a competitive gymnast. Mira graduated from Kestrov Academy of Sport with a bachelor degree in Kinesiology and Sports Science. For more than 20 years, Mira has worked as choreographer, gymnastics coach, and fitness professional.</p>
      <p>Mira has a deep knowledge (theory and experience) in many aspects of wellness including spirituality, nutrition, rehabilitation and is working towards a Physical Therapist degree.</p>
      <span class="btn btn-dark">READ MORE</span>
    </div>
  </div>
</section>

<div class="photo photo-stretch" role="img" aria-label="Trainer holding a side plank outdoors"></div>

<section class="services">
  <div class="wrap">
    <div class="service">
      <svg class="hex" width="150" height="170" viewBox="0 0 150 170"><polygon points="75,2 148,44 148,126 75,168 2,126 2,44" fill="none" stroke="#fff" stroke-width="3"/></svg>
      <svg class="icon" width="56" height="60" viewBox="0 0 56 60"><circle cx="28" cy="34" r="22" fill="none" stroke="#222" stroke-width="3.5"/><rect x="22" y="2" width="12" height="6" fill="#222"/><line x1="28" y1="8" x2="28" y2="12" stroke="#222" stroke-width="3"/><path d="M28 34 L28 16 A18 18 0 0 1 46 34 Z" fill="#222"/></svg>
      <h3>Personal Training</h3>
      <p>Private sessions will provide you with the motivation you need to reach your goals. As a fully certified trainer, Mira will make sure you're working out safely and keep the workouts fresh and exciting so you can achieve your goals.</p>
      <span class="btn btn-outline">READ MORE</span>
    </div>
    <div class="service">
      <svg class="hex" width="150" height="170" viewBox="0 0 150 170"><polygon points="75,2 148,44 148,126 75,168 2,126 2,44" fill="none" stroke="#fff" stroke-width="3"/></svg>
      <svg class="icon" width="60" height="50" viewBox="0 0 60 50"><circle cx="22" cy="28" r="17" fill="none" stroke="#222" stroke-width="3.5"/><circle cx="22" cy="28" r="5" fill="#222"/><path d="M22 11 L56 11 L56 22 L36 22" fill="none" stroke="#222" stroke-width="3.5"/></svg>
      <h3>Group Classes</h3>
      <p>Qorela Group Exercise classes are designed for people of all fitness levels. Qorela's group classes take a holistic approach and make sure you work out in a balanced way that feeds your body and spirit.</p>
      <span class="btn btn-outline">READ MORE</span>
    </div>
  </div>
</section>

<section class="videos">
  <h2>Educational Videos</h2>
  <div class="video-row">
    <div class="video v1" role="img" aria-label="Video still: exercise on a stability ball outdoors"><svg width="60" height="60" viewBox="0 0 60 60"><circle cx="30" cy="30" r="27" fill="none" stroke="#fff" stroke-width="3"/><polygon points="24,18 42,30 24,42" fill="#fff"/></svg></div>
    <div class="video v2" role="img" aria-label="Video still: sneakers on a wooden floor"><svg width="60" height="60" viewBox="0 0 60 60"><circle cx="30" cy="30" r="27" fill="none" stroke="#fff" stroke-width="3"/><polygon points="24,18 42,30 24,42" fill="#fff"/></svg></div>
    <div class="video v3" role="img" aria-label="Video still: indoor group workout"><svg width="60" height="60" viewBox="0 0 60 60"><circle cx="30" cy="30" r="27" fill="none" stroke="#fff" stroke-width="3"/><polygon points="24,18 42,30 24,42" fill="#fff"/></svg></div>
  </div>
</section>

<section class="news">
  <div class="wrap">
    <h2>News &amp; Advices</h2>
    <div class="news-row">
      <article class="news-item">
        <h4>Morbi diam mauris viverra</h4>
        <p>in gravida eu mattis in ante Morbi eget arcu Morbi porta libero id ullamcorper nonummy nibh ligula pulvinar metus eget t placerat molestie Donec dictum lectus non le</p>
        <a href="#">READ MORE</a>
      </article>
      <article class="news-item">
        <h4>Donec dictum lectus no</h4>
        <p>in gravida eu mattis in ante Morbi eget arcu Morbi porta libero id ullamcorper nonummy nibh ligula pulvinar metus eget molestie Donec dictum lectus non</p>
        <a href="#">READ MORE</a>
      </article>
      <article class="news-item">
        <h4>Cum sociis natoque penatibus et magnis dis parturient</h4>
        <p>Morbi porta libero id ullamcorper nonummy nibh ligula pulvinar metus molestie Donec dictum lectus non que habitant</p>
        <a href="#">READ MORE</a>
      </article>
    </div>
  </div>
</section>

<div class="photo photo-team" role="img" aria-label="Group of smiling exercisers stretching in a park"></div>

<section class="newsletter">
  <div class="wrap">
    <h3>Newsletter <span>Subscribe</span></h3>
    <input type="text" placeholder="Name">
    <input type="text" placeholder="Email address">
    <span class="btn btn-teal">SUBSCRIBE</span>
  </div>
</section>

<footer class="footer">
  <div class="wrap">
    <div class="footer-nav">
      <a href="#">GROUP CLASSES</a>
      <a href="#">PERSONAL TRAINING</a>
      <a href="#">ABOUT QORELA</a>
      <a href="#">BLOG</a>
      <a href="#">CONTACT</a>
    </div>
    <small>© 2016 Company Name  All right reserved  Term of Use</small>
    <div class="social"><i></i><i></i><i></i><i></i></div>
  </div>
</footer>

</body>
</html>
```